【サイトマップ】
①TOP
②初めての方へ
③医師の紹介
④訪問診療について
⑤グループワーク
⑥漢方治療
⑦うつ病・双極性障害
⑧統合失調症
⑨認知症
⑩不安障害
⑪PMS・PMDD
⑫睡眠障害
⑬心身症
⑭発達障害
⑮お知らせ (一覧)
⑯お知らせ (詳細)
⑰ブログ (一覧)
⑱ブログ (詳細)
⑲お問い合せ・FAQ
⑳採用情報

【押していきたいメニュー】
⑥漢方治療
⑪PMS・PMDD

【デザインカラー】
ピンクなど淡い色合いにしていただければと存じます。

【デザインテイスト】
①清潔感
②優しい
③ナチュラル
※派手さやゴージャスなど敷居が高くなるイメージはNG×

【フォント】
游ゴシックか游明朝を使用してください。

【参考サイト(イメージに近いサイト)】
https://kaede-heart.example/

■参考にしたい部分
・優しさを感じるデザイン
・ユーザー目線を考えた構成(情報の分かりやすさ)

【ワイヤーフレーム】
http://hoshiweb.example.jp/client-check/tsubakiyume/wireframe/01
※構成は変えていただいて問題ございません。
またサイトマップと異なる情報が入っている箇所がございます。
サイトマップが最新情報となりますので、サイトマップの方に合わせてください。

【ロゴ】
http://hoshiweb.example.jp/client-check/tsubakiyume/rogo/10.A

【院の素材】
開業前なので、素材がございません。
清潔感があり、落ち着いている雰囲気を出し、
診療場所は完全個室の予定です。

【ブログ】
下記が開業に向け、書いているブログです。
もしデザイン作成に役立つ箇所がございましたら、
参考にしていただければ幸いです。
http://tsubaki487.example/

ピクセラ[ https://jp.pixela-stock.example/ ]で定期契約をしています。
クレジット購入のみのもの以外をご利用下さい。
また定期契約のものは弊社の負担となり、ランサー様に負担はありません。
カンプ画像を入れてください。
お世話になっております。
数多くのデザイン案を見てみたいので、
延長いたします。
皆様どうぞよろしくお願いいたします。

要望を的確に読み取って頂き、
一番近いデザインにしていただきました。

この度は当院のwebサイトTOPページを作成いただきまして誠にありがとうございます。
イメージしていたデザインよりもいいものができました。

また機会がございましたらぜひよろしくお願いいたします。

```html
<!DOCTYPE html>
<html lang="ja">
<head>
<meta charset="utf-8">
<title>つばきゆめクリニック</title>
<link rel="stylesheet" href="https://fonts.googleapis.com/css2?family=Noto+Sans+JP:wght@400;500;700&family=Noto+Serif+JP:wght@400;600&display=swap">
<style>
:root{
  --pink:#ef8fb1;
  --pink-deep:#e46c98;
  --pink-soft:#fbe3ec;
  --pink-pale:#fdf1f5;
  --green:#8cc35a;
  --green-pale:#eef6e4;
  --text:#555;
  --muted:#888;
  --line:#eee;
  --white:#fff;
}
*{margin:0;padding:0;box-sizing:border-box}
html,body{width:1200px;height:3468px;overflow:hidden}
body{font-family:"Noto Sans JP",sans-serif;color:var(--text);background:var(--white);font-size:13px;position:relative}
.frame{position:absolute;inset:0;border:10px solid var(--pink-soft);pointer-events:none;z-index:5}
.serif{font-family:"Noto Serif JP",serif}
section{position:relative}

/* header */
.header{height:88px;display:flex;align-items:center;justify-content:space-between;padding:0 44px}
.brand{display:flex;align-items:center;gap:10px}
.brand-mark{width:30px;height:30px;border-radius:50%;background:var(--pink)}
.brand-name{font-size:22px;font-weight:500;color:var(--pink-deep)}
.brand-sub{font-size:10px;color:var(--muted);margin-top:2px}
.header-lead{font-size:11px;color:var(--muted)}
.header-contact{text-align:right;font-size:11px;color:var(--muted)}
.header-tel{font-size:24px;color:var(--pink-deep);font-weight:500;line-height:1.2}
.nav{height:32px;display:flex;justify-content:center;gap:0;border-bottom:1px solid var(--line)}
.nav a{width:150px;text-align:center;font-size:13px;color:var(--text);text-decoration:none;line-height:32px;border-right:1px solid var(--line)}
.nav a:first-child{border-left:1px solid var(--line)}
.nav a.current{background:var(--pink-soft);color:var(--pink-deep)}

/* hero */
.hero{height:352px;background:linear-gradient(90deg,#d9d2cf 0%,#f2ede9 45%,#fbe1ea 80%,#f7c9d8 100%)}
.hero-photo{position:absolute;inset:0}
.hero-circle{position:absolute;right:150px;top:70px;width:200px;height:200px;border-radius:50%;background:rgba(255,255,255,.92);display:flex;flex-direction:column;align-items:center;justify-content:center;text-align:center}
.hero-circle h1{font-size:22px;font-weight:400;color:var(--pink-deep);line-height:1.5}
.hero-circle p{font-size:13px;margin-top:10px;line-height:1.6}
.hero-circle em{font-style:normal;color:var(--pink-deep)}

/* news */
.news{margin:8px 40px 0;height:40px;background:var(--pink);display:flex;align-items:center;padding:0 14px;color:var(--white)}
.news-label{background:var(--white);color:var(--pink-deep);font-size:12px;padding:3px 16px;border-radius:3px}
.news-date{margin-left:24px;font-size:12px}
.news-text{margin-left:20px;font-size:12px;flex:1}
.news-more{border:1px solid var(--white);font-size:11px;padding:3px 14px;border-radius:12px}

/* worries */
.worries{height:360px;padding-top:40px}
.worries-box{width:720px;margin:0 auto;border-top:1px dashed #ddd;padding-top:34px;position:relative}
.worries-title{display:flex;align-items:center;justify-content:center;gap:14px;font-size:22px;color:var(--pink-deep)}
.clover{width:48px;height:48px}
.worries-list{display:grid;grid-template-columns:repeat(3,1fr);gap:18px 30px;margin-top:34px;list-style:none}
.worries-list li{display:flex;align-items:center;gap:8px;font-size:14px;border-bottom:1px dotted #ddd;padding-bottom:8px}
.tick{width:16px;height:16px;flex:none}
.pencil{position:absolute;right:-150px;top:0;width:110px;height:120px;background:linear-gradient(135deg,#fbd9e5,#f3aac3);border-radius:8px}

/* features */
.features{height:372px;text-align:center;padding-top:10px}
.sec-title{font-size:26px;font-weight:400;color:#444}
.sec-title small{display:block;font-family:"Noto Sans JP",sans-serif;font-size:10px;color:var(--pink);letter-spacing:.2em;margin-top:2px}
.feature-list{display:flex;justify-content:center;gap:70px;margin-top:30px}
.feature{width:220px}
.feature-label{font-size:14px;color:var(--pink-deep);border-bottom:1px solid var(--pink);display:inline-block;padding-bottom:4px}
.feature-photo{width:180px;height:180px;border-radius:50%;margin:14px auto 16px}
.feature p{font-size:12px;line-height:1.8;color:var(--muted)}

/* symptoms */
.symptoms{height:440px;background:var(--pink-pale);text-align:center;padding-top:50px}
.symptom-grid{display:grid;grid-template-columns:repeat(3,220px);gap:22px 40px;justify-content:center;margin-top:34px}
.pill{height:42px;border-radius:21px;background:var(--pink);color:var(--white);font-size:14px;line-height:42px;position:relative}
.pill::after{content:"";position:absolute;right:18px;top:17px;width:6px;height:6px;border-top:1.5px solid #fff;border-right:1.5px solid #fff;transform:rotate(45deg)}
.btn-outline{display:inline-block;margin-top:34px;border:1px solid #ccc;background:var(--white);font-size:11px;color:var(--muted);padding:6px 26px;border-radius:16px}

/* photo links */
.photo-links{height:228px;display:flex;margin-top:12px}
.photo-link{flex:1;position:relative}
.photo-link span{position:absolute;left:20px;bottom:20px;font-size:14px;color:#444;background:rgba(255,255,255,.85);padding:4px 14px}

/* blog */
.blog{height:430px;text-align:center;padding-top:44px}
.blog-list{display:flex;justify-content:center;gap:56px;margin-top:26px}
.blog-card{width:190px;text-align:left}
.blog-thumb{height:150px;background:#cfcfcf}
.blog-date{font-size:10px;color:var(--muted);margin-top:10px}
.blog-title{font-size:12px;color:var(--pink-deep);margin-top:2px}
.btn-pink{display:inline-block;border:1px solid var(--pink);color:var(--pink-deep);font-size:11px;padding:6px 28px;border-radius:16px;margin-top:30px;background:var(--white)}

/* contact banner */
.contact{height:180px;background:linear-gradient(90deg,var(--green-pale) 0%,#f4f9ee 55%,#dceccb 100%);padding:40px 0 0 190px;margin-top:10px}
.contact h2{font-size:24px;color:var(--green);font-weight:400}
.contact p{font-size:13px;margin-top:8px}
.contact .btn-green{display:inline-block;margin-top:14px;background:var(--green);color:var(--white);font-size:13px;padding:8px 36px;border-radius:20px}
.contact-flowers{position:absolute;right:0;top:0;width:330px;height:180px;background:radial-gradient(circle at 50% 50%,#ffffff 0%,#e7f1dc 60%,#cfe4b7 100%)}

/* recruit */
.recruit{height:160px;margin:60px 150px 0;background:linear-gradient(90deg,#eef6fb,#f7fbfd);display:flex;align-items:center}
.recruit-photo{width:260px;height:160px;background:linear-gradient(135deg,#dbe8f0,#f1f6f9)}
.recruit-body{padding-left:40px}
.recruit h2{font-size:24px;font-weight:400;color:#3f8bbf}
.recruit p{font-size:12px;color:var(--muted);margin-top:6px}
.recruit .btn-blue{display:inline-block;margin-top:12px;border:1px solid #3f8bbf;color:#3f8bbf;font-size:11px;padding:5px 26px;border-radius:14px;background:#fff}

/* map */
.map{height:220px;margin-top:40px;background:linear-gradient(135deg,#e8ece6,#dde4da 50%,#eef0ec)}

/* footer */
.footer{height:428px;background:var(--pink-pale);padding:30px 120px 0;display:flex;gap:80px}
.footer-info{width:520px}
.footer-info address{font-style:normal;font-size:12px;margin-top:14px}
.hours{width:100%;border-collapse:collapse;margin-top:14px;font-size:11px;background:var(--white)}
.hours th,.hours td{border:1px solid #eccfd9;padding:6px 4px;text-align:center}
.hours th{background:var(--pink);color:#fff;font-weight:400}
.footer-tel{font-size:26px;color:var(--pink-deep);margin-top:14px}
.footer-btn{display:inline-block;margin-top:8px;background:var(--pink);color:#fff;font-size:12px;padding:7px 30px;border-radius:18px}
.footer-links{display:flex;gap:60px;margin-top:20px}
.footer-links ul{list-style:none}
.footer-links li{font-size:12px;line-height:2.1}
.footer-links li::before{content:"›";color:var(--pink);margin-right:6px}
.copyright{position:absolute;left:0;right:0;bottom:0;height:28px;line-height:28px;text-align:center;font-size:10px;color:var(--muted);background:var(--pink-soft)}
</style>
</head>
<body>
<div class="frame"></div>

<header class="header">
  <div class="brand">
    <span class="brand-mark"></span>
    <div><div class="brand-name">つばきゆめクリニック</div><div class="brand-sub">Tsubaki Yume Clinic</div></div>
  </div>
  <div class="header-lead">一人ひとりの心に寄り添う地域のメンタルクリニックです</div>
  <div class="header-contact">ご予約・お問い合わせはこちら<div class="header-tel">tel.00-000-0000</div>診療時間 9:00〜18:00</div>
</header>
<nav class="nav">
  <a class="current">TOP</a><a>初めての方へ</a><a>医師の紹介</a><a>訪問診療について</a><a>グループワーク</a><a>漢方治療</a>
</nav>

<section class="hero">
  <div class="hero-photo" role="img" aria-label="寄り添い手を重ねる写真と桜の花"></div>
  <div class="hero-circle serif">
    <h1>一人で抱えて<br>いませんか？</h1>
    <p>あなたの<em>こころ</em>の<br>お手伝いを</p>
  </div>
</section>

<div class="news">
  <span class="news-label">お知らせ</span>
  <span class="news-date">2018.00.00</span>
  <span class="news-text">開院のお知らせを掲載しました</span>
  <span class="news-more">一覧を見る</span>
</div>

<section class="worries">
  <div class="worries-box">
    <h2 class="worries-title serif">
      <svg class="clover" viewBox="0 0 48 48"><g fill="#8cc35a"><circle cx="17" cy="17" r="9"/><circle cx="31" cy="17" r="9"/><circle cx="17" cy="31" r="9"/><circle cx="31" cy="31" r="9"/></g><path d="M24 24 L34 44" stroke="#6fa646" stroke-width="2"/></svg>
      このようなお悩みはございませんか？
    </h2>
    <ul class="worries-list">
      <li><svg class="tick" viewBox="0 0 16 16"><path d="M2 8l4 4 8-9" fill="none" stroke="#ef8fb1" stroke-width="2"/></svg>気分が落ち込む</li>
      <li><svg class="tick" viewBox="0 0 16 16"><path d="M2 8l4 4 8-9" fill="none" stroke="#ef8fb1" stroke-width="2"/></svg>眠れない</li>
      <li><svg class="tick" viewBox="0 0 16 16"><path d="M2 8l4 4 8-9" fill="none" stroke="#ef8fb1" stroke-width="2"/></svg>やる気が出ない</li>
      <li><svg class="tick" viewBox="0 0 16 16"><path d="M2 8l4 4 8-9" fill="none" stroke="#ef8fb1" stroke-width="2"/></svg>集中力が続かない</li>
      <li><svg class="tick" viewBox="0 0 16 16"><path d="M2 8l4 4 8-9" fill="none" stroke="#ef8fb1" stroke-width="2"/></svg>食欲がない</li>
      <li><svg class="tick" viewBox="0 0 16 16"><path d="M2 8l4 4 8-9" fill="none" stroke="#ef8fb1" stroke-width="2"/></svg>不安とイライラが続く</li>
      <li><svg class="tick" viewBox="0 0 16 16"><path d="M2 8l4 4 8-9" fill="none" stroke="#ef8fb1" stroke-width="2"/></svg>動悸・息苦しい</li>
      <li><svg class="tick" viewBox="0 0 16 16"><path d="M2 8l4 4 8-9" fill="none" stroke="#ef8fb1" stroke-width="2"/></svg>疲労感</li>
      <li><svg class="tick" viewBox="0 0 16 16"><path d="M2 8l4 4 8-9" fill="none" stroke="#ef8fb1" stroke-width="2"/></svg>対人関係がうまくいかない</li>
    </ul>
    <div class="pencil" role="img" aria-label="ピンクの鉛筆とメモのイラスト"></div>
  </div>
</section>

<section class="features">
  <h2 class="sec-title serif">当院の特徴<small>FEATURE</small></h2>
  <div class="feature-list">
    <div class="feature">
      <span class="feature-label">患者様に寄り添った治療</span>
      <div class="feature-photo" role="img" aria-label="穏やかに話を聞く女性の写真" style="background:linear-gradient(135deg,#dfe9ef,#f4f0ee)"></div>
      <p>お一人おひとりの気持ちに<br>寄り添い丁寧に診察いたします。</p>
    </div>
    <div class="feature">
      <span class="feature-label">完全個室による診療</span>
      <div class="feature-photo" role="img" aria-label="白衣の医師の写真" style="background:linear-gradient(135deg,#eef0f2,#dfe3e6)"></div>
      <p>周囲を気にせず安心して<br>お話しいただける環境です。</p>
    </div>
    <div class="feature">
      <span class="feature-label">丁寧な対応</span>
      <div class="feature-photo" role="img" aria-label="書類に記入する手元の写真" style="background:linear-gradient(135deg,#f3eee9,#e6ddd5)"></div>
      <p>ご不明な点はどんなことでも<br>お気軽にご相談ください。</p>
    </div>
  </div>
</section>

<section class="symptoms">
  <h2 class="sec-title serif">症状一覧<small>SYMPTOMS</small></h2>
  <div class="symptom-grid">
    <div class="pill">うつ病・双極性障害</div><div class="pill">統合失調症</div><div class="pill">認知症</div>
    <div class="pill">不安障害</div><div class="pill">PMS・PMDD</div><div class="pill">睡眠障害</div>
    <div class="pill">心身症</div><div class="pill">発達障害</div><div class="pill">漢方治療</div>
  </div>
  <span class="btn-outline">一覧を見る ›</span>
</section>

<section class="photo-links">
  <div class="photo-link" role="img" aria-label="明るい院内の廊下の写真" style="background:linear-gradient(135deg,#e6eef2,#cfdde4)"><span>当院について</span></div>
  <div class="photo-link" role="img" aria-label="待合室の写真" style="background:linear-gradient(135deg,#f1ece6,#ddd3c8)"></div>
  <div class="photo-link" role="img" aria-label="スタッフの写真" style="background:linear-gradient(135deg,#eef1f4,#d9e0e6)"><span>初めての方へ</span></div>
  <div class="photo-link" role="img" aria-label="診察室の写真" style="background:linear-gradient(135deg,#f2f1ef,#dedbd6)"><span>医師のご紹介</span></div>
</section>

<section class="blog">
  <h2 class="sec-title serif">ブログ<small>BLOG</small></h2>
  <div class="blog-list">
    <div class="blog-card"><div class="blog-thumb"></div><div class="blog-date">2018.00.00</div><div class="blog-title">開院準備について</div></div>
    <div class="blog-card"><div class="blog-thumb"></div><div class="blog-date">2018.00.00</div><div class="blog-title">こころの休め方のお話</div></div>
    <div class="blog-card"><div class="blog-thumb"></div><div class="blog-date">2018.00.00</div><div class="blog-title">季節の変わり目と体調</div></div>
  </div>
  <span class="btn-pink">ブログ一覧 ›</span>
</section>

<section class="contact">
  <h2 class="serif">お気軽にお問い合わせください</h2>
  <p>平日・夜・土・日曜・祝日も受付しています</p>
  <span class="btn-green">お問い合わせはこちら</span>
  <div class="contact-flowers" role="img" aria-label="白い花と若葉の写真"></div>
</section>

<section class="recruit">
  <div class="recruit-photo" role="img" aria-label="笑顔のスタッフたちの写真"></div>
  <div class="recruit-body">
    <h2 class="serif">スタッフ募集</h2>
    <p>私たちと一緒に働きませんか？まずはお気軽にご連絡ください。</p>
    <span class="btn-blue">詳細はこちら ›</span>
  </div>
</section>

<section class="map" role="img" aria-label="クリニック周辺の地図"></section>

<footer class="footer">
  <div class="footer-info">
    <div class="brand"><span class="brand-mark"></span><div><div class="brand-name">つばきゆめクリニック</div><div class="brand-sub">Tsubaki Yume Clinic</div></div></div>
    <address>〒000-0000 ○○県○○市○○町0-0-0 ○○ビル2階</address>
    <table class="hours">
      <tr><th>診療時間</th><th>月</th><th>火</th><th>水</th><th>木</th><th>金</th><th>土</th><th>日</th></tr>
      <tr><td>9:00〜12:30</td><td>●</td><td>●</td><td>●</td><td>●</td><td>●</td><td>●</td><td>―</td></tr>
      <tr><td>14:00〜18:00</td><td>●</td><td>●</td><td>―</td><td>●</td><td>●</td><td>―</td><td>―</td></tr>
    </table>
    <div class="footer-tel">tel.00-000-0000</div>
    <span class="footer-btn">お問い合わせ</span>
  </div>
  <div class="footer-links">
    <ul><li>TOP</li><li>初めての方へ</li><li>医師の紹介</li><li>訪問診療について</li><li>グループワーク</li><li>漢方治療</li><li>お知らせ</li><li>ブログ</li><li>お問い合わせ・FAQ</li><li>採用情報</li></ul>
    <ul><li>うつ病・双極性障害</li><li>統合失調症</li><li>認知症</li><li>不安障害</li><li>PMS・PMDD</li><li>睡眠障害</li><li>心身症</li><li>発達障害</li></ul>
  </div>
  <div class="copyright">Copyright © Tsubaki Yume Clinic All Rights Reserved.</div>
</footer>
</body>
</html>
```